Flyer designen DIN lang (9,8 x 21 cm): food/ event
Zielgruppe
Wir von Stadtgenuss bieten kulinarisch-kulturelle Stadtführungen in Deutschland an. Zurzeit bieten wir unserer Touren in 20 Städten an.
Aufgabenstellung
Wir brauchen einen neuen Flyer, da zum einen das Design etwas veraltet ist und zum anderen immer mehr Städte dazu kommen.
Was drauf sein sollte:
- Schönes Bild am besten mit Menschen die essen und Spaß haben (siehe Materialien/ Downoalds) oder Bildvorrat etc.
- Stadtgenuss Logo
- Text:
a) prägnant: Tickets online www.stadtgenuss-touren.de
b) Teaser auf:
1. Verschenken Sie uns als Gutschein (evtl. mit Bild vom Gutschein)
2. Möchten Sie auch Gäste begeistern? Bewerben Sie sich als Tourguide!
- Städte-Auflistung: Augsburg, Bamberg, Berlin, Bonn, Bremen, Dresden, Düsseldorf, Essen, Frankfurt, Hamburg, Hannover, Köln, Leipzig, München, Münster, Nürnberg, Oldenburg, Potsdam, Regensburg und Stuttgart
>> die Städte sollten gut erweiterbar sein, weil wir ständig wachsen.
Der bisherigen Flyer ist im Querformat gehalten- da wir eine hohe Weiterempfehlungsrate haben, hatten wir den so gestaltet, dass er fast wie eine EInladung aussieht, also mit dem Ziel, dass man uns weiterempfiehlt un dabei den Flyer übergibt. Das nur als Info, müssen dabei nicht bleiben. Den alten Flyer haben wir zur Information mit hochgeladen.
- allgemein:
a) Info zu Geschichte, Architektur und Unterhaltung (wenn mögl. auch auf Englisch: Info about History, Architecture and Entertainment
b) Details: Wann: ganzjährig Dauer: 3 Stunden Leistung: 7 Kostproben und Broschüre
Preis: 33€, Kinden 16,50€
auf english: When: all year round Length: 3 hours Includse 7 food samples + guide Price 33€, for children 16,50€
- Überschrift: Kulinarisch-kulturelle Touren
- evtl. noch Teaser: 7 Kostproben in 3 Stunden
Wir denken, es ist zurzeit zu viel Text. Es können Bausteine weg gelassen werden. Sind gespannt auf Eure Ideen.
Es kann auch ein anderes Format als bisher genommen werden.
Wenn möglich bitte unsere Schriften verwenden (siehe Dateiupload)

```html
<!DOCTYPE html>
<html lang="de">
<head>
<meta charset="utf-8">
<title>Stadtgenuss – Flyer DIN lang</title>
<link rel="stylesheet" href="https://fonts.googleapis.com/css2?family=Overlock:ital,wght@0,400;0,700;0,900;1,700;1,900&family=Alegreya+Sans+SC:wght@400;500;700&display=swap">
<style>
  :root{
    --maroon:#983d3f;
    --orange:#f0a22c;
    --orange-light:#f6b94c;
    --cream:#fdf2e3;
    --ink-light:#fff8ec;
    --stage:#eeeeee;
  }
  *{box-sizing:border-box;margin:0;padding:0}
  html,body{width:1200px;height:1200px;overflow:hidden}
  body{
    background:radial-gradient(circle at 50% 35%,#fbfbfb 0%,var(--stage) 70%);
    font-family:"Overlock",sans-serif;
    position:relative;
  }
  .flyer{
    position:absolute;left:100px;width:1000px;height:467px;
    overflow:hidden;box-shadow:0 10px 30px rgba(0,0,0,.18);
  }
  .flyer--front{top:100px;background:var(--cream)}
  .flyer--back{top:633px;background:linear-gradient(100deg,var(--orange-light),var(--orange))}
  .flyer svg.art{position:absolute;inset:0;width:1000px;height:467px}

  /* front */
  .front-text{position:absolute;left:370px;top:28px;right:28px}
  .brand{font-weight:700;font-size:30px;color:var(--maroon);text-align:right;padding-right:40px;line-height:1.1}
  .headline-kicker{font-weight:900;font-style:italic;font-size:44px;color:var(--orange);line-height:1;margin-top:10px;text-align:right;padding-right:10px}
  .headline{font-weight:900;font-size:172px;line-height:.86;color:var(--maroon);letter-spacing:-2px;margin-top:4px}
  .teaser{font-weight:700;font-style:italic;font-size:32px;color:var(--orange);text-align:right;margin-top:-6px;padding-right:8px}
  .cities{font-family:"Alegreya Sans SC",sans-serif;font-size:18px;color:var(--maroon);line-height:1.25;margin-top:10px;font-weight:500}
  .tagline-en{font-family:"Alegreya Sans SC",sans-serif;font-size:15px;color:var(--maroon);text-align:right;margin-top:6px}

  /* back */
  .back-content{position:absolute;left:380px;top:28px;right:26px;color:var(--ink-light)}
  .info-cols{display:grid;grid-template-columns:1fr 1fr;gap:28px}
  .info-title{font-weight:900;font-size:34px;color:var(--maroon);line-height:1}
  .info-topics{font-family:"Alegreya Sans SC",sans-serif;font-size:15px;letter-spacing:.5px;margin-top:2px}
  .details-title{font-weight:900;font-size:34px;color:var(--maroon);line-height:1;margin-top:8px}
  .details-title--spacer{visibility:hidden}
  .details{display:grid;grid-template-columns:auto 1fr;column-gap:10px;row-gap:6px;margin-top:10px;padding-bottom:10px;border-bottom:1px dashed rgba(255,248,236,.7)}
  .details dt{font-family:"Alegreya Sans SC",sans-serif;font-size:13px;opacity:.9}
  .details dd{font-size:13px}
  .details .pair{display:contents}
  .voucher-row{display:flex;gap:22px;align-items:center;margin-top:22px}
  .voucher-img{width:200px;height:110px;flex:none;border-radius:4px;transform:rotate(-6deg);box-shadow:0 4px 10px rgba(0,0,0,.2);background:linear-gradient(120deg,#7fa35a 0%,#f4ede2 55%,var(--maroon) 100%)}
  .voucher-text{font-weight:900;font-size:34px;line-height:1.02;color:var(--ink-light)}
  .tickets{font-weight:900;font-size:40px;color:var(--maroon);margin-top:16px}
  .contact{font-size:18px;font-weight:700;margin-top:2px}
</style>
</head>
<body>

<section class="flyer flyer--front" aria-label="Flyer Vorderseite">
  <svg class="art" viewBox="0 0 1000 467">
    <defs>
      <linearGradient id="heroGrad" x1="0" y1="0" x2="0" y2="1">
        <stop offset="0" stop-color="#5fa7de"/>
        <stop offset=".5" stop-color="#b8d9ef"/>
        <stop offset=".75" stop-color="#d9b77a"/>
        <stop offset="1" stop-color="#6cae3c"/>
      </linearGradient>
    </defs>
    <path role="img" aria-label="Foto: Rucksack mit Stadtplan und belegten Brötchen auf Gras vor blauem Himmel"
          d="M0 0 H300 C360 120 370 330 300 467 H0 Z" fill="url(#heroGrad)"/>
    <path d="M300 0 C360 120 370 330 300 467" fill="none" stroke="var(--orange)" stroke-width="10"/>
    <path d="M316 0 C378 120 388 330 316 467" fill="none" stroke="var(--maroon)" stroke-width="12"/>
  </svg>
  <div class="front-text">
    <p class="brand">Stadtgenuss</p>
    <p class="headline-kicker">Kulinarisch-kulturelle</p>
    <h1 class="headline">Touren</h1>
    <p class="teaser">7 Kostproben in 3 Stunden</p>
    <p class="cities">in Augsburg, Bamberg, Berlin, Bonn, Bremen, Dresden, Düsseldorf, Essen, Frankfurt, Hamburg, Hannover, Köln, Leipzig, München, Münster, Nürnberg, Oldenburg, Potsdam, Regensburg und Stuttgart</p>
    <p class="tagline-en">Walking food tour with 7 samples in 3 hours</p>
  </div>
</section>

<section class="flyer flyer--back" aria-label="Flyer Rückseite">
  <svg class="art" viewBox="0 0 1000 467">
    <defs>
      <clipPath id="collageClip">
        <path d="M0 0 H300 C360 120 370 330 300 467 H0 Z"/>
      </clipPath>
    </defs>
    <g clip-path="url(#collageClip)">
      <rect x="0" y="0" width="400" height="467" fill="#fbf3e8"/>
      <rect role="img" aria-label="Foto: Wraps mit Gemüse" x="0" y="0" width="175" height="235" fill="#c9c58a"/>
      <rect role="img" aria-label="Foto: Gäste lachen beim Essen" x="179" y="0" width="221" height="235" fill="#d9c4b4"/>
      <rect role="img" aria-label="Foto: Teller mit Vorspeisen" x="0" y="239" width="175" height="228" fill="#e6b98e"/>
      <rect role="img" aria-label="Foto: Tischrunde in einem Restaurant" x="179" y="239" width="221" height="228" fill="#b9aca2"/>
    </g>
    <path d="M300 0 C360 120 370 330 300 467" fill="none" stroke="var(--ink-light)" stroke-width="10"/>
    <path d="M316 0 C378 120 388 330 316 467" fill="none" stroke="var(--maroon)" stroke-width="12"/>
  </svg>
  <div class="back-content">
    <div class="info-cols">
      <div class="info-col">
        <h2 class="info-title">Info zu</h2>
        <p class="info-topics">Geschichte, Architektur &amp; Unterhaltung</p>
        <p class="details-title details-title--spacer" aria-hidden="true">Details</p>
        <dl class="details">
          <div class="pair"><dt>Wann</dt><dd>ganzjährig</dd></div>
          <div class="pair"><dt>Dauer</dt><dd>3 Stunden</dd></div>
          <div class="pair"><dt>Leistung</dt><dd>7 Kostproben und Broschüre</dd></div>
          <div class="pair"><dt>Preis</dt><dd>33€, Kinder 16,50€</dd></div>
        </dl>
      </div>
      <div class="info-col">
        <h2 class="info-title">Info about</h2>
        <p class="info-topics">History, Architecture &amp; Entertainment</p>
        <h2 class="details-title">Details</h2>
        <dl class="details">
          <div class="pair"><dt>When</dt><dd>all year round</dd></div>
          <div class="pair"><dt>Length</dt><dd>3 hours</dd></div>
          <div class="pair"><dt>Include</dt><dd>7 food samples + guide</dd></div>
          <div class="pair"><dt>Price</dt><dd>33€, for children 16,50€</dd></div>
        </dl>
      </div>
    </div>
    <div class="voucher-row">
      <div class="voucher-img" role="img" aria-label="Bild eines Gutscheins"></div>
      <p class="voucher-text">Verschenken Sie uns<br>als Gutschein</p>
    </div>
    <p class="tickets">Tickets Online</p>
    <p class="contact">www.stadtgenuss-touren.de • Tel +49 (0)30 - 555 01 234 0</p>
  </div>
</section>

</body>
</html>
```